The Corvane Agency

We are a pr, social media and strategy agency specializing in the pet industry. We would like a new dynamic design of our existing website. We think it is currently outdated and looks too corporate. We would like it to look more consumer oriented as we primarily market pet products. We would like warm imagery involving pets and while pets are fun, this is still a business website and needs to maintain a professional look. We are hired by business owners and executives.
I would like some of our work featured on the home page.
Our primary service tabs are:
Public Relations
Social Media
Product Consulting
Most of the content will remain the same but we are open to suggestions!
Our current website can be found at www.corvanepetpr.example.
We are open to other colors than in our logo and on our current page.
This is a design only project and will not require programming. The selected designer will need to provide at least one interior page in addition to the home page.

Industry/Entity Type

Pet

Requirements
Should not have
• Cartoon type figures. Pet puns.

```html
<!DOCTYPE html>
<html lang="en">
<head>
<meta charset="utf-8">
<title>The Corvane Agency</title>
<link href="https://fonts.googleapis.com/css2?family=Oswald:wght@200;300;400;500&family=Arvo:wght@700&family=Open+Sans:wght@400;600&display=swap" rel="stylesheet">
<style>
:root{
  --orange:#f26a0f;
  --yellow:#fdc851;
  --amber:#f7a21b;
  --green:#8cc63f;
  --ink:#222;
  --grey:#666;
  --title-grey:#8a8a8a;
  --line:#e6e6e6;
  --frame:#e9e9e9;
}
*{margin:0;padding:0;box-sizing:border-box}
html,body{width:784px;height:1200px;overflow:hidden;background:#fff}
body{position:relative;font-family:Arial,Helvetica,sans-serif;color:var(--ink)}
.abs{position:absolute}
.topbar{left:0;top:0;width:784px;height:35px;background:var(--orange)}
.topbar span{position:absolute;top:4px;font:300 20px/26px Oswald,sans-serif;color:#fff}
.brand-tab{left:0;top:0}
.brand-name{left:300px;top:8px;width:184px;text-align:center;font:500 17px/22px Oswald,sans-serif;color:var(--orange)}
.hero-photo{left:16px;top:36px;width:400px;height:308px;border-radius:40% 45% 0 0;background:radial-gradient(circle at 35% 30%,#f25a1c 0,#f7b52a 40%,#c9d625 65%,#5aa832 90%)}
.hero-title{left:397px;top:156px;font:200 30px/34px Oswald,sans-serif;color:#7a7a7a;letter-spacing:-.3px;white-space:nowrap}
.hero-copy{left:399px;top:192px;width:318px;font-size:10px;line-height:12px;color:var(--grey)}
.arrow{top:167px;width:25px;height:25px;border-radius:50%;background:var(--yellow)}
.arrow svg{display:block;margin:8px}
.band{left:0;top:345px;width:784px;height:153px;background:var(--orange)}
.nav{left:0;top:332px}
.nav-item{position:absolute;top:17px;font:300 17px/24px Oswald,sans-serif;color:#fff;white-space:nowrap}
.social{position:absolute;top:412px;width:96px;text-align:center}
.social i{display:block;width:48px;height:48px;border-radius:50%;background:#fff;margin:0 auto}
.social b{display:block;margin-top:10px;font:300 12px/14px Oswald,sans-serif;color:#fff;white-space:nowrap}
.kitten{left:12px;top:544px;width:304px;height:224px;border-radius:45% 30% 10% 20%;background:radial-gradient(ellipse at 45% 50%,#b3a79a 0,#d8d0c6 55%,#fff 80%)}
.welcome{left:270px;top:544px;font:700 31px/40px Arvo,serif;color:var(--green)}
.welcome-copy{left:239px;top:588px;width:220px;font-size:9.6px;line-height:11.6px;color:var(--ink)}
.welcome-copy p+p{margin-top:12px}
.news-head{left:509px;top:533px;font:300 27px/36px Oswald,sans-serif;color:#555;letter-spacing:-.5px}
.news{position:absolute;left:506px;width:240px}
.date{position:absolute;left:0;top:0;width:40px;height:40px;border-radius:50%;background:var(--amber);color:#fff;text-align:center;font:500 18px/18px Oswald,sans-serif;padding-top:4px}
.date small{display:block;font-size:10px;line-height:10px}
.date.alt{background:var(--yellow)}
.news h3{position:absolute;left:48px;top:0;width:190px;font:500 15px/17.5px Oswald,sans-serif;color:var(--title-grey);letter-spacing:-.4px}
.news p{position:absolute;left:0;top:52px;width:240px;font-size:9.3px;line-height:14.5px;color:var(--grey)}
.news a{color:#333;font-weight:bold;text-decoration:underline}
.rule{left:26px;width:728px;height:1px;background:var(--line)}
.card{position:absolute;top:857px;width:170px}
.card .frame{width:120px;height:91px;background:var(--frame);padding:8px}
.card .frame div{width:104px;height:75px}
.card h4{margin-top:10px;font:400 12.5px/15px "Open Sans",sans-serif;color:#333}
.card p{margin-top:19px;font-size:9.4px;line-height:11.6px;color:var(--grey)}
.more{right:30px;top:1091px;font:600 13px/18px "Open Sans",sans-serif;color:#444}
.more i{display:inline-block;width:9px;height:9px;border-radius:50%;background:#888;margin-left:6px;vertical-align:0}
.footer{left:0;top:1146px;width:784px;height:54px;background:var(--orange);color:#fff;text-align:center;font-size:8.5px;line-height:54px}
.footer b{font:500 12px Oswald,sans-serif;margin-right:6px}
</style>
</head>
<body>
<header class="abs topbar">
  <span style="left:194px">Welcome to</span>
  <span style="left:498px">website.</span>
</header>
<svg class="abs brand-tab" width="784" height="60" viewBox="0 0 784 60" aria-hidden="true">
  <polygon points="300,0 484,0 502,35 484,58 300,58 282,35" fill="#fff"/>
  <polygon points="282,35 300,35 274,58" fill="#cfcfcf"/>
  <polygon points="484,35 502,35 502,58" fill="#cfcfcf"/>
</svg>
<div class="abs brand-name">The Corvane Agency</div>

<div class="abs hero-photo" role="img" aria-label="Two lovebirds with orange heads and green-yellow bodies"></div>
<div class="abs arrow" style="left:13px"><svg width="9" height="9" viewBox="0 0 9 9"><path d="M6 1 2 4.5 6 8" stroke="#f7a21b" stroke-width="1.5" fill="none"/></svg></div>
<div class="abs arrow" style="left:744px"><svg width="9" height="9" viewBox="0 0 9 9"><path d="M3 1 7 4.5 3 8" stroke="#f7a21b" stroke-width="1.5" fill="none"/></svg></div>
<h1 class="abs hero-title">REDEFINING THE PET INDUSTRY</h1>
<p class="abs hero-copy">The power of any association is the strenght of unity. We have managed a wide range of pet-related associations and tradeshows, brining teams together to deliver outstanding results.</p>

<section class="abs band"></section>
<nav class="abs nav">
  <svg width="784" height="56" viewBox="0 0 784 56" aria-hidden="true">
    <polygon points="84,0 716,0 700,13 674,56 116,56 76,13" fill="#fdc851"/>
    <polygon points="76,1 84,0 90,13 72,13" fill="#f7a21b"/>
    <polygon points="700,0 716,0 710,13 700,13" fill="#f7a21b"/>
  </svg>
  <span class="nav-item" style="left:150px">HOME</span>
  <span class="nav-item" style="left:230px">PUBLIC RELATIONS</span>
  <span class="nav-item" style="left:386px">SOCIAL MEDIA</span>
  <span class="nav-item" style="left:516px">PRODUCT CONSULTING</span>
</nav>
<div class="social" style="left:98px"><i></i><b>LIKE US</b></div>
<div class="social" style="left:198px"><i></i><b>FOLLOW US</b></div>
<div class="social" style="left:294px"><i></i><b>CORVANE LIFE</b></div>
<div class="social" style="left:390px"><i></i><b>CONNECT WITH US</b></div>
<div class="social" style="left:486px"><i></i><b>OUR BLOG</b></div>
<div class="social" style="left:578px"><i></i><b>CORPORATE SITE</b></div>

<div class="abs kitten" role="img" aria-label="Tabby kitten crouching playfully"></div>
<h2 class="abs welcome">WELCOME!</h2>
<div class="abs welcome-copy">
  <p>Praesent vestibulum molestie lacus. Aeneanum nonummy hendrerit mauris. Phasellus portame. Fusce suscipit varius mium sociis natoquemetun penatibus et magnis dis parturient.</p>
  <p>Montes, nascetur ridiculus mus. Nulla dui. Fusce feugiat &nbsp;malesuada odio morbi nunc odio gravida atem cursus nluctus lorem maecenas tristique orci ac sem. Duis ultricies pharetra.</p>
</div>

<h2 class="abs news-head">LATEST NEWS</h2>
<article class="news" style="top:586px">
  <div class="date">25<small>JUL</small></div>
  <h3>FUSCE SUSCIPIT VARIUS MIUM SOCIIS NATOQUEMETUN</h3>
  <p>Montes, nascetur ridiculus mus. Nulla dui. Fusce feugiat &nbsp;malesuada odio morbi nunc. <a>READ MORE</a></p>
</article>
<article class="news" style="top:682px">
  <div class="date alt">25<small>JUL</small></div>
  <h3>FUSCE SUSCIPIT VARIUS MIUM SOCIIS NATOQUEMETUN</h3>
  <p>Montes, nascetur ridiculus mus. Nulla dui. Fusce feugiat &nbsp;malesuada odio morbi nunc. <a>READ MORE</a></p>
</article>

<div class="abs rule" style="top:822px"></div>

<div class="card" style="left:38px">
  <div class="frame"><div role="img" aria-label="Woman holding a kitten" style="background:linear-gradient(135deg,#8a7a62,#c8bfb0)"></div></div>
  <h4>Nora Ellery</h4>
  <p>Montes, nascetur ridiculus mus. Nulla dui.Fusce feugiat &nbsp;malesuada odio morbi nunc odio gravida atem cursus nluctus lorem maecenas.</p>
</div>
<div class="card" style="left:229px">
  <div class="frame"><div role="img" aria-label="Smiling woman lying beside a dog" style="background:linear-gradient(135deg,#b0743f,#e2b890)"></div></div>
  <h4>Tessa Quinlan</h4>
  <p>Montes, nascetur ridiculus mus. Nulla dui.Fusce feugiat &nbsp;malesuada odio morbi nunc odio gravida atem cursus nluctus lorem maecenas.</p>
</div>
<div class="card" style="left:425px">
  <div class="frame"><div role="img" aria-label="Woman with a small white dog" style="background:linear-gradient(135deg,#c9c768,#e8e6b8)"></div></div>
  <h4>Adela Ferris</h4>
  <p>Montes, nascetur ridiculus mus. Nulla dui.Fusce feugiat &nbsp;malesuada odio morbi nunc odio gravida atem cursus nluctus lorem maecenas.</p>
</div>
<div class="card" style="left:615px">
  <div class="frame"><div role="img" aria-label="Person holding a chihuahua puppy" style="background:linear-gradient(135deg,#4cc9d0,#c07a4a)"></div></div>
  <h4>Maren Holt</h4>
  <p>Montes, nascetur ridiculus mus. Nulla dui.Fusce feugiat &nbsp;malesuada odio morbi nunc odio gravida atem nluctus lorem maecenas.</p>
</div>

<div class="abs rule" style="top:1070px"></div>
<div class="abs more">more testimonials<i></i></div>

<footer class="abs footer"><b>THE CORVANE AGENCY</b>© 2013. All Rights Reserved</footer>
</body>
</html>
```